New Zealand health product business needs website designed

A website is required for a business that sells New Zealand made products, namely products like infant formula, health products such as NZ honey, supplements, skincare products etc. This is purely an informative website that will introduce the all the different types of products the business has to offer. The target audience will the the Chinese market. The logo is a calligraphy style font in colours 78b643 and 313542 (logo is still being finalised at the moment) so a colour theme to match would be great.

It is crucial that the design communicates the beautiful nature of New Zealand, non-polluted environments, with emphasis on pure, natural and cleaniness.
Updates

A website that I quite like is http://www.frostvalegelato.co.nz

Information is easy to find, layout is nice and clear.                          

Hi all, I have now uploaded a logo for the business "Tawny Crate", please note that this is yet to be finalized however I expect it to be minor changes so please ensure the website theme and colour use go well with the logo. 

There are three scenery images uploaded, designs with any one of them used is fine whichever works better with your design.  Only one image is required on the website, no sliding effects for this.

Also just to clarify my requirements further.  The developer can use HTML, PHP, Javascript, CSS for coding, preferably to have the images cut and a pdf guide provided for things like alignment and sizing etc.

The menu items are Home / Our story / Product outline / Brands / Contact us
Designs are required for all these.  Within the product outline page, the subcategories are -
Infant formulas
Baby supplements
Toddlers products
Honey
Beauty products
Mens supplements
Womens supplements
Health products
Others

   

Target Market(s)

China based customers looking for quality products from New Zealand.

Industry/Entity Type

Health

Requirements
Must have
• clear menu bar in home page, the four main menu items are -
Our story
Product outline
Brands
Contact us
Nice to have
• Space for a large scenery photo in the home page

```html
<!DOCTYPE html>
<html lang="en">
<head>
<meta charset="utf-8">
<title>Tawny Crate – Pure New Zealand Products</title>
<link rel="stylesheet" href="https://fonts.googleapis.com/css2?family=Arimo:wght@400;700&family=Kaushan+Script&display=swap">
<style>
  :root {
    --page-bg: #000000;
    --header-bg: #30333f;
    --body-bg: #252835;
    --card-bg: #1e2029;
    --menu-bg: #21232f;
    --nav-bg: #000000;
    --rule: #7d8090;
    --divider: #9a9fbd;
    --brand-green: #78b643;
    --text-muted: #9a9ca6;
    --text-subline: #6f7280;
    --headline: #6b739e;
  }
  * { margin: 0; padding: 0; box-sizing: border-box; }
  html, body { width: 1200px; height: 1029px; overflow: hidden; }
  body { background: var(--page-bg); font-family: "Arimo", Arial, sans-serif; position: relative; }

  .site { position: absolute; left: 113px; top: 0; width: 972px; height: 1029px; background: var(--body-bg); }

  .site-header { position: absolute; left: 0; top: 0; width: 972px; height: 185px; background: var(--header-bg); }
  .brand { position: absolute; left: 115px; top: 52px; }
  .brand-name { font-size: 48px; font-weight: 700; color: var(--brand-green); line-height: 1; }
  .brand-subline { position: absolute; left: 157px; top: 110px; font-size: 18px; color: var(--text-subline); white-space: nowrap; }

  .main-nav { position: absolute; left: 0; top: 185px; width: 972px; height: 43px; background: var(--nav-bg); border-top: 2px solid var(--rule); }
  .nav-item { position: absolute; top: 8px; height: 25px; line-height: 25px; text-align: center; font-size: 16px; color: var(--text-muted); border-left: 2px solid var(--divider); }
  .nav-item.is-active { color: var(--brand-green); }
  .nav-end { position: absolute; top: 8px; left: 908px; height: 25px; border-left: 2px solid var(--divider); }

  .submenu { position: absolute; left: 288px; top: 228px; width: 189px; z-index: 3; list-style: none; }
  .submenu li { height: 40px; line-height: 40px; padding-left: 40px; background: var(--menu-bg); font-size: 16px; color: var(--text-muted); border-bottom: 2px solid var(--rule); }
  .submenu li:last-child { border-bottom: none; }
  .submenu li.is-active { color: var(--brand-green); }

  .hero { position: absolute; left: 0; top: 228px; width: 972px; height: 455px; border-bottom: 2px solid var(--rule); }
  .hero-photo { position: absolute; inset: 0; background: linear-gradient(180deg, #f6dfa3 0%, #f3c35a 30%, #d8a94a 44%, #a0783a 60%, #6e5128 78%, #5a4220 100%); }
  .hero-title { position: absolute; left: 78px; top: 38px; font-family: "Kaushan Script", cursive; font-size: 48px; color: var(--headline); white-space: nowrap; }
  .hero-lead { position: absolute; left: 84px; top: 107px; font-size: 20px; color: var(--headline); white-space: nowrap; }

  .topics { position: absolute; left: 66px; top: 725px; width: 846px; height: 159px; }
  .topic-rule { position: absolute; top: 0; width: 2px; height: 159px; background: var(--divider); }
  .topic { position: absolute; top: 0; width: 189px; height: 157px; background: var(--card-bg); }
  .topic-photo { width: 189px; height: 85px; }
  .topic-title { margin: 12px 0 0 8px; font-size: 14px; font-weight: 700; color: var(--brand-green); }
  .topic-text { margin: 4px 6px 0 8px; font-size: 14px; line-height: 18px; color: var(--text-muted); }

  .social { position: absolute; left: 155px; top: 959px; display: flex; gap: 12px; }
  .social-link { width: 27px; height: 27px; border-radius: 3px; display: block; }
  .social-a { background: #3b5a9a; }
  .social-b { background: #e4e6e8; }
  .social-c { background: #c4302b; }
</style>
</head>
<body>
<div class="site">
  <header class="site-header">
    <div class="brand"><span class="brand-name">Tawny Crate</span></div>
    <p class="brand-subline">Subline logo this is the subline</p>
  </header>

  <nav class="main-nav">
    <span class="nav-item" style="left:69px;width:206px;">Our story</span>
    <span class="nav-item is-active" style="left:279px;width:210px;">Product outline</span>
    <span class="nav-item" style="left:489px;width:210px;">Brands</span>
    <span class="nav-item" style="left:699px;width:211px;">Contact us</span>
    <span class="nav-end"></span>
  </nav>

  <ul class="submenu">
    <li>item 1</li>
    <li class="is-active">item 2</li>
    <li>item 3</li>
    <li>item 4</li>
  </ul>

  <section class="hero">
    <div class="hero-photo" role="img" aria-label="Golden sunrise over a beach with large round boulders in the surf"></div>
    <h1 class="hero-title">Clear air. Clean water. Pure nature.</h1>
    <p class="hero-lead">Quality Products from New Zealand</p>
  </section>

  <section class="topics">
    <span class="topic-rule" style="left:0;"></span>
    <article class="topic" style="left:12px;">
      <div class="topic-photo" role="img" aria-label="Coastal rocks by turquoise water" style="background:linear-gradient(180deg,#3aa3a0,#a88a5c 55%,#5a8c74);"></div>
      <h2 class="topic-title">Topic 1</h2>
      <p class="topic-text">Lorem ipsum dolor sit amet, consectetuer adipiscing...</p>
    </article>
    <span class="topic-rule" style="left:210px;"></span>
    <article class="topic" style="left:222px;">
      <div class="topic-photo" role="img" aria-label="Smooth pebbles under clear water" style="background:linear-gradient(135deg,#8a7a6e,#b5a89a 50%,#6e5a52);"></div>
      <h2 class="topic-title">Topic 2</h2>
      <p class="topic-text">Lorem ipsum dolor sit amet, consectetuer adipiscing...</p>
    </article>
    <span class="topic-rule" style="left:420px;"></span>
    <article class="topic" style="left:432px;">
      <div class="topic-photo" role="img" aria-label="Green and grey river stones" style="background:linear-gradient(135deg,#1f5a58,#4f8d84 50%,#2a4a48);"></div>
      <h2 class="topic-title">Topic 3</h2>
      <p class="topic-text">Lorem ipsum dolor sit amet, consectetuer adipiscing...</p>
    </article>
    <span class="topic-rule" style="left:630px;"></span>
    <article class="topic" style="left:644px;">
      <div class="topic-photo" role="img" aria-label="Rippled silver water surface" style="background:linear-gradient(160deg,#6e6e72,#c9cacd 50%,#55565a);"></div>
      <h2 class="topic-title">Topic 4</h2>
      <p class="topic-text">Lorem ipsum dolor sit amet, consectetuer adipiscing...</p>
    </article>
    <span class="topic-rule" style="left:840px;"></span>
  </section>

  <footer class="social">
    <span class="social-link social-a" role="img" aria-label="Social network link"></span>
    <span class="social-link social-b" role="img" aria-label="Professional network link"></span>
    <span class="social-link social-c" role="img" aria-label="Video channel link"></span>
  </footer>
</div>
</body>
</html>
```